Business Card Design

We need a business card design for a new company based in Allen, Texas. (outside of Dallas,Texas) We offer Business Management Solutions to Entrepreneurs, as well as Corporate Businesses. Our product line offers solutions to Image, Branding, Social Media marketing, business development strategies, banking / funding solutions, just to name a few. We would like to see designs that convey strength and confidence. I have attached a sample design of our company name. Designers you may use company name as either: Vorlix or Vorlix Corporation, depending on the design layout.

Please show alternate color of Black as well.

Industry/Entity Type

Business

Contact Information for Business Card

Vorlix Corporation

2847 E. Hollowbrook Drive, STE 410
Larkmoor, TX 75091
Office: 469.318.7742
Fax: 469.318.7743

Dr. Miles Dunworth
Business Development Director

```html
<!DOCTYPE html>
<html lang="en">
<head>
<meta charset="utf-8">
<title>Vorlix Corporation – Business Card</title>
<link href="https://fonts.googleapis.com/css2?family=Arimo:wght@400;700&display=swap" rel="stylesheet">
<style>
  :root {
    --backdrop: #e4e4e4;
    --ink: #1c1c1c;
    --card-dark: #262626;
    --card-light: #efefef;
    --rule-light: #eaeaea;
    --text-soft: #2a2a2a;
  }
  * { margin: 0; padding: 0; box-sizing: border-box; }
  html, body { width: 1200px; height: 900px; overflow: hidden; }
  body {
    background: var(--backdrop);
    font-family: "Arimo", Arial, sans-serif;
    position: relative;
  }
  .card {
    position: absolute;
    width: 556px;
    height: 357px;
    border-radius: 22px;
    overflow: hidden;
  }
  .card--front { left: 333px; top: 48px; background: var(--card-dark); color: var(--rule-light); }
  .card--back { left: 335px; top: 440px; background: var(--card-light); color: var(--ink); }

  .rule { position: absolute; left: 0; right: 0; height: 4px; }
  .card--front .rule { background: var(--rule-light); }
  .card--front .rule--top { top: 72px; }
  .card--front .rule--bottom { top: 275px; }
  .card--back .rule { background: var(--ink); top: 70px; }

  .front-wordmark {
    position: absolute; left: 0; right: 0; top: 116px;
    text-align: center; font-size: 98px; font-weight: 400;
    letter-spacing: 1px; line-height: 1;
  }
  .front-tagline {
    position: absolute; left: 50%; top: 264px; transform: translateX(-50%);
    background: var(--card-dark); padding: 0 6px;
    font-size: 20px; letter-spacing: 0.5px; line-height: 26px;
  }

  .back-brand { position: absolute; left: 40px; width: 224px; top: 136px; text-align: center; }
  .back-wordmark { font-size: 60px; line-height: 1; letter-spacing: 0.5px; }
  .back-tagline { font-size: 15px; font-weight: 700; margin-top: 34px; letter-spacing: 0.3px; }

  .divider { position: absolute; left: 275px; top: 125px; width: 3px; height: 150px; background: var(--ink); }

  .person { position: absolute; left: 314px; top: 122px; }
  .person-name { font-size: 19px; font-weight: 700; letter-spacing: 0.2px; }
  .person-title { font-size: 13px; margin-top: 4px; color: var(--text-soft); }

  .contact-list { position: absolute; left: 313px; top: 178px; list-style: none; }
  .contact-list li { display: flex; align-items: center; height: 26.5px; font-size: 14px; }
  .contact-list svg { width: 18px; height: 14px; margin-right: 14px; fill: var(--ink); }

  .address {
    position: absolute; left: 0; right: 0; top: 301px;
    display: flex; justify-content: center; align-items: center;
    font-size: 14px;
  }
  .address svg { width: 16px; height: 15px; fill: var(--ink); margin-right: 2px; }
</style>
</head>
<body>
  <section class="card card--front" aria-label="Card front">
    <div class="rule rule--top"></div>
    <div class="front-wordmark">vorlix</div>
    <div class="rule rule--bottom"></div>
    <div class="front-tagline">CORPORATION</div>
  </section>

  <section class="card card--back" aria-label="Card back">
    <div class="rule"></div>
    <div class="back-brand">
      <div class="back-wordmark">vorlix</div>
      <div class="back-tagline">CORPORATION</div>
    </div>
    <div class="divider"></div>
    <div class="person">
      <div class="person-name">Dr. MILES DUNWORTH</div>
      <div class="person-title">Business Development Director</div>
    </div>
    <ul class="contact-list">
      <li>
        <svg viewBox="0 0 18 14" aria-hidden="true"><path d="M1 4c0-2 3-3 8-3s8 1 8 3v1h-4V3.5H5V5H1z"/><rect x="3" y="6" width="12" height="7" rx="1"/></svg>
        469.318.7742
      </li>
      <li>
        <svg viewBox="0 0 18 14" aria-hidden="true"><rect x="4" y="0" width="10" height="4"/><rect x="1" y="5" width="16" height="6" rx="1"/><rect x="4" y="9" width="10" height="5" fill="#fff" stroke="#1c1c1c"/></svg>
        469.318.7743
      </li>
      <li>
        <svg viewBox="0 0 18 14" aria-hidden="true"><path d="M2 2h14v10H2z"/><path d="M2 2l7 6 7-6" fill="none" stroke="#efefef" stroke-width="1.4"/></svg>
        mdunworth@vorlixmail.com
      </li>
      <li>
        <svg viewBox="0 0 18 14" aria-hidden="true"><circle cx="7" cy="7" r="6" fill="none" stroke="#1c1c1c" stroke-width="1.4"/><path d="M1 7h12M7 1v12" stroke="#1c1c1c" stroke-width="1"/><path d="M12 10l5 4" stroke="#1c1c1c" stroke-width="2"/></svg>
        www.VorlixCorp.com
      </li>
    </ul>
    <div class="address">
      <svg viewBox="0 0 16 15" aria-hidden="true"><path d="M8 0l8 7h-2v8H10v-5H6v5H2V7H0z"/></svg>
      2847 E. Hollowbrook Drive, STE 410 Larkmoor, TX 75091
    </div>
  </section>
</body>
</html>
```